Strata management company needs someone who specialise in wordpress to help complete the current web

We need a website design for a strata management company based in Sydney Australia. We provide strata management services to the local strata titled buildings. We have got logo and website contents(copywriting) completed. And we have got a basic layout and framework developed based on wordpress. Now we need someone who specialize in wordpress to help us optimize the website to be a professional looking and SEO friendly site. Please refer to the following URL for the current layout. Please note the website is going to be in both English and Chinese . Need to have the backend for both English and Chinese website provided by wordpress. (I can do the translation in Chinese if you need something to be translated on the coding part) We will also provide the contents translated in Chinese. The website needs to have clear navigation and uprunning smoothly.

We have paid for coding package as well. Please do necessary coding if required to make the website look professional and work smoothly without bugs.

www.pelwaroveproperty.com.au/home-3

Target Market(s)

Developers of new buildings or owners of existing buildings with strata title

Industry/Entity Type

It Company

Coding

Coded - Design and coding required

Number of Pages Required

5+ page

Font styles to use
Sans Serif

Requirements
Must have
• 1)have both English and Chinese backend as shown on http://pelwaroveproperty.com.au/home-3/
• 2) Color scheme must match the logo color
• 3) Clear navigation: specific group of customers can find the service tailored to them easily. (developer of residential/mixed use property and commercial/industrial property. owner of residential/mixed use property and commercial/industrial property)
• 4) Professional looking: layout, pictures, font etc. and professional banner picture on the top
• 5) SEO friendly
Nice to have
• make the website warm, can engage with target audiences.
• Can interact with customers easily. As you can see, we have divided to the customers to two major groups: developers and owners. Under developers there are developer of residential/mixed use property and commercial/industrial property. Under owners there are owner of residential/mixed use property and commercial/industrial property.
Should not have
• bugs, breaking pages

```html
<!DOCTYPE html>
<html lang="en">
<head>
<meta charset="utf-8">
<title>Repairs &amp; Maintenance – Pelwarove Strata Management</title>
<link href="https://fonts.googleapis.com/css2?family=Mulish:wght@400;500;600&family=Open+Sans:wght@400&display=swap" rel="stylesheet">
<style>
:root{
  --yellow:#f7b928;
  --footer-a:#eda623;
  --footer-b:#f8bd2e;
  --red:#e8302b;
  --ink:#111111;
  --body:#555555;
  --white:#ffffff;
  --muted:#8a8a8a;
  --footer-text:#5a3e0c;
}
*{margin:0;padding:0;box-sizing:border-box}
html,body{width:953px;height:1200px;overflow:hidden;background:var(--white)}
body{position:relative;font-family:"Mulish",sans-serif;color:var(--ink)}

/* header */
.site-header{position:absolute;left:0;top:0;width:953px;height:88px;background:var(--white)}
.brand{position:absolute;display:flex;align-items:center;gap:8px}
.brand-mark{width:56px;height:56px;border-radius:50%;background:var(--red);flex:none}
.brand-name{font-family:"Mulish",sans-serif;font-weight:600;color:var(--ink);line-height:1.15}
.brand-name .big{display:block;font-size:22px}
.brand-name .small{display:block;font-size:12px}
.header-brand{left:96px;top:10px}
.member-login{position:absolute;left:644px;top:38px;width:118px;height:31px;border-radius:16px;background:#000;color:var(--white);font-size:11.5px;font-weight:500;display:flex;align-items:center;justify-content:center;white-space:nowrap}
.language{position:absolute;left:772px;top:46px;font-size:10.5px;color:var(--muted)}
.flag{position:absolute;left:832px;top:44px;width:26px;height:17px;background:var(--red)}

/* nav */
.main-nav{position:absolute;left:0;top:88px;width:953px;height:42px;background:var(--yellow)}
.nav-item{position:absolute;top:0;height:42px;line-height:42px;font-size:13px;font-weight:500;color:var(--ink);text-transform:uppercase;white-space:nowrap}
.nav-item.active{background:var(--red);color:var(--white);width:179px;text-align:center;font-size:12.6px}
.search-field{position:absolute;left:682px;top:9px;width:153px;height:22px;background:var(--white)}
.search-btn{position:absolute;left:835px;top:9px;width:23px;height:22px;background:var(--red)}

/* hero */
.hero{position:absolute;left:0;top:130px;width:953px;height:270px;background:linear-gradient(100deg,#6a6e72 0%,#4a5a70 35%,#5a5f63 60%,#6b625a 100%)}
.hero-title{position:absolute;left:0;top:112px;width:953px;text-align:center;color:var(--white);font-size:33px;font-weight:600;letter-spacing:.3px}

/* content */
.content-title{position:absolute;left:97px;top:451px;font-size:27px;font-weight:400}
.content-body{position:absolute;left:95px;top:496px;width:466px;font-family:"Open Sans",sans-serif;font-size:10.3px;line-height:14.4px;color:var(--body)}
.content-body p{margin-bottom:16.8px}
.content-photo{position:absolute;left:570px;top:458px;width:290px;height:319px;background:linear-gradient(135deg,#c98f6a 0%,#e8d8cc 40%,#e66a4a 70%,#ece8e4 100%)}

/* footer */
.site-footer{position:absolute;left:0;top:866px;width:953px;height:334px;background:linear-gradient(120deg,var(--footer-a),var(--footer-b))}
.footer-brand{left:90px;top:40px}
.footer-about{position:absolute;left:94px;top:116px;width:215px;font-size:10.6px;line-height:18.5px;color:var(--footer-text)}
.social{position:absolute;left:94px;top:183px;display:flex;gap:1px}
.social span{width:26px;height:26px;border:1.2px solid var(--white);border-radius:50%}
.footer-col{position:absolute;top:52px}
.footer-col h3{font-size:17.5px;font-weight:400;margin-bottom:13px;letter-spacing:.2px}
.footer-col a{display:block;font-size:13px;line-height:24px;color:var(--ink);text-decoration:none;white-space:nowrap}
.contact-row{position:relative;padding-left:26px;font-size:13px;line-height:23.5px;white-space:nowrap}
.contact-row svg{position:absolute;left:2px;top:5px}
.divider{position:absolute;left:90px;top:264px;width:765px;height:1px;background:rgba(255,255,255,.35)}
.copyright{position:absolute;left:0;top:286px;width:936px;text-align:center;font-size:10.5px;color:var(--footer-text)}
</style>
</head>
<body>

<header class="site-header">
  <div class="brand header-brand">
    <span class="brand-mark"></span>
    <span class="brand-name"><span class="big">Pelwarove</span><span class="small">Strata Management</span></span>
  </div>
  <div class="member-login">Member Login</div>
  <div class="language">Language:</div>
  <div class="flag"></div>
</header>

<nav class="main-nav">
  <span class="nav-item" style="left:111px">Home</span>
  <span class="nav-item" style="left:184px">About Us</span>
  <span class="nav-item" style="left:275px">Services</span>
  <span class="nav-item active" style="left:346px">Repair &amp; Maintenance</span>
  <span class="nav-item" style="left:538px">News</span>
  <span class="nav-item" style="left:602px">Contact</span>
  <div class="search-field"></div>
  <div class="search-btn">
    <svg width="23" height="22" viewBox="0 0 23 22"><circle cx="10.5" cy="10" r="3.8" fill="none" stroke="#fff" stroke-width="1.8"/><line x1="13.3" y1="12.8" x2="16" y2="15.5" stroke="#fff" stroke-width="2"/></svg>
  </div>
</nav>

<section class="hero" role="img" aria-label="Tradesmen repairing a wall and floor inside a building">
  <h1 class="hero-title">REPAIRS &amp; MAINTENANCE</h1>
</section>

<main>
  <h2 class="content-title">Repairs &amp; Maintenance</h2>
  <div class="content-body">
    <p>A swift response and early attention to requests for repairs and maintenance is an extremely important function of your strata manager.</p>
    <p>During business hours – 9.00am to 5.00pm please phone your strata manager to advise details of required repairs and maintenance, alternatively you may email details on martin@pelwaroveproperty.com.au. After hours emergencies should be advised through our office phone number which will be re directed to our after hours tradesmen.<br>Tenants should contact their property manager or owner to advise necessary repairs.</p>
    <p>Usually all emergencies will be attended to by the afterhours tradesmen if possible and repairs completed without reference to the owners corporation, normally these repairs will be covered by insurance. Any emergencies which cannot rectified immediately will be made safe and secure and work completed during business hours.</p>
    <p>3 quotes will be obtained for non urgent repairs. For small repairs we suggest an agreed limit should be set between the strata management and the executive committee.</p>
    <p>We guarantee all our tradesmen are licensed and have current public liability and workers compensation insurance policies. This procedure ensures that the owners corporation have little exposure to liability claims.</p>
  </div>
  <div class="content-photo" role="img" aria-label="Two workers in red and orange caps laying floorboards beside a brick wall"></div>
</main>

<footer class="site-footer">
  <div class="brand footer-brand">
    <span class="brand-mark"></span>
    <span class="brand-name"><span class="big">Pelwarove</span><span class="small">Strata Management</span></span>
  </div>
  <p class="footer-about">Asociosqu ad litora torquent per conubia nostra per inceptos hymenaeos Proin nulla arcu nonummy luctus dictum</p>
  <div class="social"><span></span><span></span><span></span><span></span></div>

  <div class="footer-col" style="left:333px">
    <h3>COMPANY</h3>
    <a>Home</a><a>About Us</a><a>Services</a><a>Why Choose Us</a><a>Blogs</a>
  </div>
  <div class="footer-col" style="left:490px">
    <h3>RESOURCES</h3>
    <a>FAQ</a><a>Repairs &amp; Maintenance</a><a>Our Team</a><a>Member Login</a><a>Contact Us</a>
  </div>
  <div class="footer-col" style="left:652px">
    <h3>CONTACT</h3>
    <div class="contact-row">
      <svg width="12" height="16" viewBox="0 0 12 16"><path d="M6 1a5 5 0 0 0-5 5c0 3.8 5 9 5 9s5-5.2 5-9a5 5 0 0 0-5-5z" fill="#fff"/><circle cx="6" cy="6" r="1.8" fill="#f3b02a"/></svg>
      Suite4, Level3, 218 Marlow<br>St., Westbury NSW2150
    </div>
    <div class="contact-row">
      <svg width="16" height="15" viewBox="0 0 16 15"><path d="M3 1l3 3-1.6 1.8c.9 2 2.5 3.7 4.6 4.6L10.8 9l3 3-1.8 2C6.5 13.6 1.5 8.6 1 3z" fill="none" stroke="#fff" stroke-width="1.2" stroke-linejoin="round"/></svg>
      02 9000 4172
    </div>
    <div class="contact-row">
      <svg width="15" height="12" viewBox="0 0 15 12"><rect x="1" y="1" width="13" height="10" fill="none" stroke="#fff" stroke-width="1.2"/><path d="M1 1l6.5 5.5L14 1" fill="none" stroke="#fff" stroke-width="1.2"/></svg>
      info@pelwaroveproperty.com.au
    </div>
  </div>

  <div class="divider"></div>
  <p class="copyright">© 2017 Company Name&nbsp; All right reserved</p>
</footer>

</body>
</html>
```